Pulsewell Power sharing solutions, we offer different types of mobile charging stations for all ty

I need an app that shows all the locations that use our charging stations.
the app should show the following:

1. a map where client can see where all the stations are
2. a map that shows which one is the nearest charging station based on the persons location
3. a search tab where you can pick the city ( all will be based from sweden) and we will start with two cities: Gothenburg and Stockholm. So user will be able to pick the city and than get a list of all venues using our stations. along the way we will keep adding cities and countries but for now i need a design, something i can show potential customers on a power point how this app will work.
4. a list of different venue categories:
- restaurant
- café
- Festival
- Airport
- Library
- Night club
- Shopping center

Once client chooses the city, they can also choose what they are looking for and choose for example which restaurant to eat at based on if they have our charging station or not

you can of course improvise on ideas, if you come up with something and want to add to the app design thats ok, I'm up for suggestions.

in conclusion: the purpose for the app is for users to be able to search for charging stations or see where the nearest charging station is

Target Market(s)

Everyone

Requirements
Must have
• professional and simple design

```html
<!DOCTYPE html>
<html lang="en">
<head>
<meta charset="utf-8">
<title>Pulsewell Power – Charging Station Finder</title>
<link rel="stylesheet" href="https://fonts.googleapis.com/css2?family=Cabin:wght@400;500&family=PT+Sans:wght@400;700&family=PT+Sans+Narrow:wght@400;700&family=Nunito:wght@800&display=swap">
<style>
  :root {
    --page-bg: #f1f1f1;
    --bar-dark: #45484a;
    --panel-mid: #56595b;
    --panel-body: #4e5153;
    --panel-list: #6d7274;
    --rule-light: #d9dcdd;
    --text-light: #ffffff;
    --text-dark: #1d1d1b;
    --accent-yellow: #f5d327;
    --accent-orange: #f7a823;
    --map-base: #d9c3c1;
    --pin-dark: #2b2c2e;
    --pin-light: #5a5c5f;
  }
  * { box-sizing: border-box; margin: 0; padding: 0; }
  html, body { width: 1200px; height: 962px; overflow: hidden; }
  body { background: var(--page-bg); font-family: "PT Sans", Arial, sans-serif; position: relative; }

  .screen {
    position: absolute; top: 228px; width: 300px; height: 537px;
    background: var(--panel-body); overflow: hidden;
  }
  .screen--all { left: 72px; }
  .screen--nearest { left: 450px; }
  .screen--search { left: 830px; }

  .top-bar {
    height: 76px; background: var(--bar-dark);
    display: flex; align-items: center; justify-content: space-between; padding: 0 22px 0 26px;
  }
  .top-bar svg { display: block; }

  .map { background: linear-gradient(160deg, #e0cccb, var(--map-base)); }
  .map--overview { position: absolute; left: 4px; top: 80px; width: 292px; height: 252px; border: 3px solid #fff; }
  .map--nearest { position: absolute; left: 0; top: 267px; width: 300px; height: 270px; }
  .map--search { position: absolute; left: 0; top: 466px; width: 300px; height: 71px; filter: blur(1px); }

  .station-pin { position: absolute; display: block; filter: drop-shadow(1px 2px 1px rgba(0,0,0,0.25)); }

  .action-band {
    position: absolute; left: 0; width: 300px; background: var(--accent-yellow);
    color: var(--text-dark); text-align: center;
  }
  .action-band--all { top: 342px; height: 60px; line-height: 60px; font-size: 22px; letter-spacing: 0.3px; }
  .action-band--nearest { top: 204px; height: 63px; padding-top: 10px; }
  .action-band__title { font-family: "PT Sans Narrow", sans-serif; font-weight: 700; font-size: 25px; line-height: 26px; }
  .action-band__sub { font-family: "PT Sans Narrow", sans-serif; font-weight: 700; font-size: 10px; letter-spacing: 0.5px; text-transform: uppercase; }

  .location-panel { position: relative; height: 128px; background: var(--panel-mid); color: var(--text-light); }
  .location-panel__pin { position: absolute; left: 38px; top: 22px; }
  .location-panel__label { position: absolute; left: 74px; top: 26px; font-family: "Cabin", sans-serif; font-size: 14px; }
  .location-panel__city {
    position: absolute; left: 74px; top: 44px; width: 182px; font-family: "Cabin", sans-serif;
    font-size: 33px; line-height: 42px; border-top: 1px solid var(--rule-light); padding-top: 2px;
  }
  .location-panel__city::after { content: ""; display: block; border-bottom: 1px solid var(--rule-light); margin-top: 3px; }
  .location-panel__toggle { position: absolute; right: 12px; bottom: 8px; }

  .category-list { position: absolute; top: 204px; left: 0; width: 300px; height: 195px; background: var(--panel-list); list-style: none; padding: 18px 0 0 48px; }
  .category-list__item {
    display: flex; align-items: center; height: 42px; color: var(--text-light);
    font-size: 15px; text-transform: uppercase; letter-spacing: 0.3px;
  }
  .category-list__plus { width: 22px; font-size: 24px; font-weight: 700; line-height: 1; }
  .category-list__name { margin-left: 14px; width: 182px; border-bottom: 1px solid var(--rule-light); padding-bottom: 3px; }
  .category-list__toggle { position: absolute; right: 12px; bottom: 10px; }

  .submit-button {
    position: absolute; top: 399px; left: 0; width: 300px; height: 67px; border: 0;
    background: linear-gradient(90deg, var(--accent-yellow), var(--accent-orange));
    color: var(--text-light); font-family: "Nunito", sans-serif; font-weight: 800; font-size: 31px;
  }
</style>
</head>
<body>

<svg width="0" height="0" style="position:absolute">
  <defs>
    <linearGradient id="pin-shade" x1="0" y1="0" x2="1" y2="0">
      <stop offset="0" stop-color="#5a5c5f"/>
      <stop offset="0.5" stop-color="#2b2c2e"/>
      <stop offset="1" stop-color="#1a1b1c"/>
    </linearGradient>
    <symbol id="station-pin" viewBox="0 0 30 44">
      <path d="M15 0C6.7 0 0 6.7 0 15c0 11 15 29 15 29s15-18 15-29C30 6.7 23.3 0 15 0z" fill="url(#pin-shade)"/>
      <circle cx="15" cy="15" r="6.5" fill="#ffffff"/>
    </symbol>
  </defs>
</svg>

<!-- Screen 1: all charging stations -->
<section class="screen screen--all">
  <header class="top-bar">
    <svg class="icon-menu" width="30" height="22" viewBox="0 0 30 22"><g fill="#1b1b1b"><rect width="30" height="5" rx="1"/><rect y="8.5" width="30" height="5" rx="1"/><rect y="17" width="30" height="5" rx="1"/></g></svg>
    <svg class="icon-user" width="24" height="30" viewBox="0 0 24 30"><g fill="#1b1b1b"><circle cx="12" cy="8" r="7.5"/><path d="M0 30v-6c0-5 4-8 8-8h8c4 0 8 3 8 8v6z"/></g></svg>
  </header>
  <div class="map map--overview" role="img" aria-label="City street map with markers for every charging station">
    <svg class="station-pin" style="left:86px;top:50px" width="17" height="25"><use href="#station-pin"/></svg>
    <svg class="station-pin" style="left:232px;top:20px" width="17" height="25"><use href="#station-pin"/></svg>
    <svg class="station-pin" style="left:219px;top:140px" width="17" height="25"><use href="#station-pin"/></svg>
    <svg class="station-pin" style="left:16px;top:201px" width="17" height="25"><use href="#station-pin"/></svg>
    <svg class="station-pin" style="left:135px;top:130px" width="40" height="58"><use href="#station-pin"/></svg>
  </div>
  <div class="action-band action-band--all">ALL CHARGING STATIONS</div>
</section>

<!-- Screen 2: nearest station -->
<section class="screen screen--nearest">
  <header class="top-bar">
    <svg class="icon-menu" width="30" height="22" viewBox="0 0 30 22"><g fill="#1b1b1b"><rect width="30" height="5" rx="1"/><rect y="8.5" width="30" height="5" rx="1"/><rect y="17" width="30" height="5" rx="1"/></g></svg>
    <svg class="icon-user" width="24" height="30" viewBox="0 0 24 30"><g fill="#1b1b1b"><circle cx="12" cy="8" r="7.5"/><path d="M0 30v-6c0-5 4-8 8-8h8c4 0 8 3 8 8v6z"/></g></svg>
  </header>
  <div class="location-panel">
    <svg class="location-panel__pin" width="22" height="32" viewBox="0 0 22 32"><path d="M11 0C5 0 0 5 0 11c0 8 11 21 11 21s11-13 11-21C22 5 17 0 11 0z" fill="#fff"/><circle cx="11" cy="11" r="4.5" fill="var(--panel-mid)"/></svg>
    <div class="location-panel__label">Location Obtained</div>
    <div class="location-panel__city">Gothenburg</div>
    <svg class="location-panel__toggle" width="14" height="9" viewBox="0 0 14 9"><path d="M0 0h14L7 9z" fill="#2e3032"/></svg>
  </div>
  <div class="action-band action-band--nearest">
    <div class="action-band__title">NEAREST STATION</div>
    <div class="action-band__sub">Take Me Here</div>
  </div>
  <div class="map map--nearest" role="img" aria-label="Street map centred on the nearest charging station">
    <svg class="station-pin" style="left:141px;top:88px" width="50" height="74"><use href="#station-pin"/></svg>
  </div>
</section>

<!-- Screen 3: search by city and venue -->
<section class="screen screen--search">
  <header class="top-bar">
    <svg class="icon-menu" width="30" height="22" viewBox="0 0 30 22"><g fill="#1b1b1b"><rect width="30" height="5" rx="1"/><rect y="8.5" width="30" height="5" rx="1"/><rect y="17" width="30" height="5" rx="1"/></g></svg>
    <svg class="icon-user" width="24" height="30" viewBox="0 0 24 30"><g fill="#1b1b1b"><circle cx="12" cy="8" r="7.5"/><path d="M0 30v-6c0-5 4-8 8-8h8c4 0 8 3 8 8v6z"/></g></svg>
  </header>
  <div class="location-panel">
    <svg class="location-panel__pin" width="22" height="32" viewBox="0 0 22 32"><path d="M11 0C5 0 0 5 0 11c0 8 11 21 11 21s11-13 11-21C22 5 17 0 11 0z" fill="#fff"/><circle cx="11" cy="11" r="4.5" fill="var(--panel-mid)"/></svg>
    <div class="location-panel__label">Search Your City</div>
    <div class="location-panel__city">Gothenburg</div>
    <svg class="location-panel__toggle" width="14" height="9" viewBox="0 0 14 9"><path d="M0 0h14L7 9z" fill="#2e3032"/></svg>
  </div>
  <ul class="category-list">
    <li class="category-list__item"><span class="category-list__plus">+</span><span class="category-list__name">Restaurant</span></li>
    <li class="category-list__item"><span class="category-list__plus">+</span><span class="category-list__name">Airport</span></li>
    <li class="category-list__item"><span class="category-list__plus">+</span><span class="category-list__name">Shopping Center</span></li>
    <li class="category-list__item"><span class="category-list__plus">+</span><span class="category-list__name">Café</span></li>
    <svg class="category-list__toggle" width="14" height="9" viewBox="0 0 14 9"><path d="M0 9h14L7 0z" fill="#3a3d3f"/></svg>
  </ul>
  <button class="submit-button" type="button">Submit!</button>
  <div class="map map--search" role="img" aria-label="Street map showing matching venues"></div>
</section>

</body>
</html>
```